Brevan Law Business cards and stationary design project

We are looking for a stationary design for business cards (double sided), 8x10, 5x7, and legal and standard envelopes.

We would like the design to match the logo that we have already.
Color palate preferred is Teal, White, grey and any others that will look good for a professional law firm.

We would like this statement: "RELATIONSHIPS. RESPECT. RESULT" to be on the back of the business cards and maybe on the stationary if it looks good.

Please see link to website for more information: www.brevan-law-example.com

Target Market(s)

Potential clients that need Attorney services.

Industry/Entity Type

Law Firm

Contact Information for Business Card

We would like the front and back to be two different colors. Current business cards are teal front, grey back and are a vertical design. We are open to options with colors.

Font styles to use
Serif

Colors
33a6d7
33b8a4
b9b9b9
5c5c5c

Requirements
Must have
• Logo supplied needs to go on the card and stationary.
• Match website color palate, www.brevan-law-example.com
• Be professional and not too wordy.
• Criminal Law, Civil Litigation, Personal Injury, Restraining Orders need to be on the card.
Nice to have
• RELATIONSHIPS. RESPECT. RESULTS. on the back of the card.
Should not have
• Not be too busy/wordy or too flashy.

```html
<!DOCTYPE html>
<html lang="en">
<head>
<meta charset="utf-8">
<title>Brevan Law — Business Card</title>
<link rel="stylesheet" href="https://fonts.googleapis.com/css2?family=Cinzel:wght@400;500&family=Crimson+Text:wght@400&display=swap">
<style>
  :root {
    --teal: #10889a;
    --white: #ffffff;
    --backdrop: #e4e5e6;
    --card-edge: rgba(0, 0, 0, 0.12);
  }
  * { box-sizing: border-box; margin: 0; padding: 0; }
  html, body {
    width: 1105px;
    height: 1200px;
    overflow: hidden;
    background: var(--backdrop);
  }
  .stage {
    position: relative;
    width: 1105px;
    height: 1200px;
  }
  .card {
    position: absolute;
    left: 196px;
    width: 720px;
    height: 410px;
    box-shadow: 0 1px 3px var(--card-edge);
  }
  .card--front { top: 146px; background: var(--teal); color: var(--white); }
  .card--back  { top: 602px; background: var(--white); color: var(--teal); }

  .firm-name {
    position: absolute;
    font-family: "Cinzel", serif;
    font-weight: 400;
    white-space: nowrap;
  }
  .card--front .firm-name {
    left: 569px;
    top: 138px;
    transform: translateX(-50%);
    font-size: 34px;
    letter-spacing: 1px;
    color: var(--white);
  }
  .card--back .firm-name {
    left: 50%;
    top: 150px;
    transform: translateX(-50%);
    font-size: 58px;
    letter-spacing: 2px;
    color: var(--teal);
  }

  .holder {
    position: absolute;
    left: 39px;
    top: 218px;
  }
  .holder__name {
    font-family: "Cinzel", serif;
    font-weight: 500;
    font-size: 30px;
    line-height: 1;
    letter-spacing: 1px;
  }
  .holder__title {
    margin-top: 8px;
    font-family: "Cinzel", serif;
    font-weight: 400;
    font-size: 19px;
    line-height: 1;
    letter-spacing: 1px;
  }

  .contact {
    position: absolute;
    left: 39px;
    top: 295px;
    list-style: none;
  }
  .contact__item {
    display: flex;
    align-items: center;
    height: 30.5px;
    font-family: "Crimson Text", serif;
    font-size: 21px;
  }
  .contact__icon {
    width: 18px;
    height: 18px;
    margin-right: 15px;
    flex: none;
  }

  .tagline {
    position: absolute;
    left: 0;
    right: 0;
    top: 352px;
    text-align: center;
    font-family: "Cinzel", serif;
    font-weight: 400;
    font-size: 21px;
    letter-spacing: 0.5px;
    color: var(--teal);
  }
</style>
</head>
<body>
<main class="stage">
  <section class="card card--front" aria-label="Business card front">
    <div class="firm-name">Brevan Law</div>

    <div class="holder">
      <div class="holder__name">Maren Castell</div>
      <div class="holder__title">Trial Lawyer</div>
    </div>

    <ul class="contact">
      <li class="contact__item">
        <svg class="contact__icon" viewBox="0 0 24 24" aria-hidden="true">
          <path fill="#fff" d="M6.6 10.8c1.4 2.8 3.8 5.1 6.6 6.6l2.2-2.2c.3-.3.7-.4 1-.2 1.1.4 2.3.6 3.6.6.6 0 1 .4 1 1V20c0 .6-.4 1-1 1C10.6 21 3 13.4 3 4c0-.6.4-1 1-1h3.5c.6 0 1 .4 1 1 0 1.3.2 2.5.6 3.6.1.3 0 .7-.2 1z"/>
        </svg>
        (555) 014-2286
      </li>
      <li class="contact__item">
        <svg class="contact__icon" viewBox="0 0 24 24" aria-hidden="true">
          <rect x="2" y="5" width="20" height="14" fill="#fff"/>
          <path d="M2 5l10 8 10-8" fill="none" stroke="#10889a" stroke-width="1.6"/>
        </svg>
        maren@brevan-law-example.com
      </li>
      <li class="contact__item">
        <svg class="contact__icon" viewBox="0 0 24 24" aria-hidden="true">
          <circle cx="12" cy="12" r="10" fill="#fff"/>
          <path d="M7 7c2 1 3 0 4 2s-2 3-1 5 2 1 2 4M15 5c-1 2 1 3 2 4s3 0 3 2" fill="none" stroke="#10889a" stroke-width="1.6"/>
        </svg>
        www.brevan-law-example.com
      </li>
    </ul>
  </section>

  <section class="card card--back" aria-label="Business card back">
    <div class="firm-name">Brevan Law</div>
    <p class="tagline">Relationships. Respect. Results.</p>
  </section>
</main>
</body>
</html>
```